Innovative Strategic IT Solutions and Management Consulting

Looking for a fresh design idea to represent a company which specializes in innovative strategic IT solutions focusing on information assurance, enterprise content management, health information technology, web applications, strategic IT solutions and solutions architect.

KELTO...the company name means "new beginning" in Greek or the acronym for Keep-Every-Layer-Tightly-Organized. We pride ourselves in understanding the client's business and needs before proposing an innovative solutions.

Innovation / Secure / Strategy - the core motto

Color: Maroon / Burgundy / Silver / White / Grey / Black

Primary focus color: Burgundy / Silver

```html
<!DOCTYPE html>
<html lang="en">
<head>
<meta charset="utf-8">
<title>KELTO – Strategic IT Solutions</title>
<link rel="stylesheet" href="https://fonts.googleapis.com/css2?family=Roboto+Condensed:wght@300;400;700&family=Montserrat:wght@400;500;600&display=swap">
<style>
  :root {
    --burgundy: #8e0f0f;
    --burgundy-dark: #6a0707;
    --ink: #111111;
    --text: #555555;
    --muted: #8a8a8a;
    --faint: #c4c4c4;
    --line: #e4e4e4;
    --panel: #f4f4f4;
    --white: #ffffff;
  }
  * { margin: 0; padding: 0; box-sizing: border-box; }
  html, body { width: 1004px; height: 1200px; overflow: hidden; background: var(--white); }
  body { font-family: "Montserrat", Arial, sans-serif; color: var(--text); }
  .page { position: relative; width: 1004px; height: 1200px; overflow: hidden; background: var(--white); }

  /* Header */
  .site-header { position: absolute; left: 0; top: 0; width: 1004px; height: 64px; background: var(--white); }
  .brand { position: absolute; left: 83px; top: 20px; display: flex; align-items: center; gap: 10px; }
  .brand-square { width: 14px; height: 14px; background: var(--burgundy); }
  .brand-name { font-family: "Montserrat", Arial, sans-serif; font-weight: 600; font-size: 22px; line-height: 24px; color: var(--burgundy); letter-spacing: 1px; }
  .main-nav a { position: absolute; top: 23px; font-size: 15px; color: #555; text-decoration: none; white-space: nowrap; }
  .main-nav a.is-active { color: var(--burgundy); font-weight: 500; }

  /* Hero */
  .hero { position: absolute; left: 0; top: 64px; width: 1004px; height: 378px;
    background: linear-gradient(90deg, #d6dadb 0%, #eef0f0 30%, #f7f8f8 55%, #e6eaec 80%, #dfe3e6 100%); }
  .hero-photo { position: absolute; left: 666px; top: 30px; width: 276px; height: 348px;
    background: linear-gradient(180deg, #eceeef 0%, #e4e2e0 45%, #d9d6d3 100%); }
  .hero-title { position: absolute; left: 83px; top: 106px; font-family: "Roboto Condensed", Arial, sans-serif; font-weight: 700; font-size: 29px; line-height: 35px; color: var(--ink); }
  .hero-subtitle { position: absolute; left: 83px; top: 190px; font-family: "Roboto Condensed", Arial, sans-serif; font-weight: 300; font-size: 32px; line-height: 38px; color: var(--burgundy); white-space: nowrap; }
  .hero-copy { position: absolute; left: 83px; top: 235px; width: 495px; font-size: 10.5px; line-height: 17px; color: #333; }
  .hero-notch { position: absolute; left: 492px; top: 432px; }

  /* Services */
  .services { position: absolute; left: 0; top: 442px; width: 1004px; height: 236px; background: var(--panel); }
  .service { position: absolute; top: 42px; width: 200px; text-align: center; }
  .service-icon { width: 52px; height: 52px; margin: 0 auto; border-radius: 50%; background: var(--white); box-shadow: 0 1px 3px rgba(0,0,0,0.12); display: flex; align-items: center; justify-content: center; }
  .service-title { height: 40px; margin-top: 16px; display: flex; align-items: center; justify-content: center; font-size: 14px; line-height: 17px; font-weight: 500; color: var(--ink); }
  .service-text { width: 178px; margin: 14px auto 0; font-size: 10.5px; line-height: 15.5px; color: var(--muted); }
  .service-divider { position: absolute; top: 82px; width: 1px; height: 108px; background: #e2e2e2; }

  /* Call to action */
  .cta-band { position: absolute; left: 0; top: 678px; width: 1004px; height: 66px;
    background: linear-gradient(90deg, #7a0606 0%, #a51414 35%, #9a0f0f 60%, #6e0505 100%); }
  .cta-text { position: absolute; left: 178px; top: 19px; font-family: "Roboto Condensed", Arial, sans-serif; font-weight: 700; font-size: 25px; line-height: 28px; color: var(--white); white-space: nowrap; }
  .cta-text .cta-lead { color: #e3c6c6; }
  .cta-arrow { position: absolute; left: 584px; top: 22px; }
  .cta-button { position: absolute; left: 656px; top: 17px; width: 122px; height: 36px; border-radius: 3px;
    background: linear-gradient(180deg, #ffffff 0%, #e4e4e4 100%); box-shadow: 0 1px 2px rgba(0,0,0,0.35);
    font-size: 13px; font-weight: 500; color: #333; letter-spacing: 0.5px; display: flex; align-items: center; justify-content: center; }

  /* Info section */
  .info-heading { position: absolute; font-size: 14.5px; font-weight: 500; color: var(--ink); white-space: nowrap; }
  .phone { position: absolute; left: 90px; top: 818px; font-size: 14.5px; font-weight: 600; color: var(--burgundy); letter-spacing: 0.6px; }
  .call-note { position: absolute; left: 70px; top: 860px; width: 127px; text-align: right; font-size: 10px; line-height: 14px; color: #555; }
  .call-link { position: absolute; left: 70px; top: 919px; width: 127px; text-align: right; font-size: 10.5px; color: var(--burgundy); }
  .column-shadow { position: absolute; left: 228px; top: 768px; width: 8px; height: 230px;
    background: linear-gradient(90deg, rgba(0,0,0,0.05), rgba(0,0,0,0)); }
  .need-lead { position: absolute; left: 263px; top: 818px; width: 170px; font-size: 12px; line-height: 18px; color: var(--burgundy); }
  .need-copy { position: absolute; left: 263px; top: 863px; width: 185px; font-size: 10px; line-height: 14px; color: #555; }
  .team-photo { position: absolute; left: 479px; top: 790px; width: 122px; height: 126px;
    background: linear-gradient(180deg, #e9eef0 0%, #d7dde0 55%, #c9cfd2 100%); }
  .quote-mark { position: absolute; left: 266px; top: 944px; }
  .quote-text { position: absolute; left: 294px; top: 951px; width: 210px; font-size: 9.5px; line-height: 14px; font-weight: 600; color: var(--ink); }
  .quote-author { position: absolute; left: 520px; top: 953px; width: 84px; text-align: right; font-size: 10px; line-height: 13px; color: #555; }
  .quote-author strong { display: block; font-weight: 600; color: var(--burgundy); }
  .link-list { position: absolute; list-style: none; }
  .link-list li { position: relative; height: 20px; padding-left: 12px; font-size: 9.5px; line-height: 14px; color: #555; white-space: nowrap; }
  .link-list li::before { content: "›"; position: absolute; left: 0; top: -1px; font-size: 12px; color: #888; }

  /* Footer */
  .footer-rule { position: absolute; left: 83px; top: 1034px; width: 839px; height: 1px; background: var(--line); }
  .footer-brand { position: absolute; left: 83px; top: 1083px; display: flex; align-items: center; gap: 9px; }
  .footer-brand-square { width: 12px; height: 12px; background: var(--faint); }
  .footer-brand-name { font-family: "Montserrat", Arial, sans-serif; font-weight: 600; font-size: 20px; line-height: 22px; color: var(--faint); letter-spacing: 1px; }
  .social-dot { position: absolute; top: 1127px; width: 10px; height: 10px; background: var(--faint); }
  .copyright { position: absolute; left: 83px; top: 1160px; font-size: 8.5px; color: var(--muted); white-space: nowrap; }
  .footer-links li { height: 20.5px; font-size: 9.5px; }
  .partner { position: absolute; background: #dcdcdc; border-radius: 3px; }
</style>
</head>
<body>
<div class="page">

  <header class="site-header">
    <div class="brand">
      <span class="brand-square"></span>
      <span class="brand-name">KELTO</span>
    </div>
    <nav class="main-nav">
      <a class="is-active" style="left:451px">Home</a>
      <a style="left:526px">About Us</a>
      <a style="left:622px">Services</a>
      <a style="left:712px">Work</a>
      <a style="left:781px">Blog</a>
      <a style="left:846px">Contact Us</a>
    </nav>
  </header>

  <section class="hero" role="img" aria-label="Bright blurred office interior with tall windows">
    <div class="hero-photo" role="img" aria-label="Smiling nurse with a stethoscope reading a tablet"></div>
    <h1 class="hero-title">Welcome to<br>Keep-Every-Layer-Tightly-Organized</h1>
    <h2 class="hero-subtitle">HEALTH INFORMATION TECHNOLOGY</h2>
    <p class="hero-copy">Lorem Ipsum is simply dummy text of the printing and typesetting industry Lorem Ipsum has been the industry's standard dummy text ever since the 1500s, when an unknown printer took a galley of type and scrambled it to make</p>
  </section>

  <section class="services">
    <div class="service" style="left:69px">
      <div class="service-icon">
        <svg width="20" height="18" viewBox="0 0 20 18" aria-hidden="true"><rect x="2" y="3" width="16" height="10" fill="none" stroke="var(--burgundy)" stroke-width="1.6"/><line x1="7" y1="16" x2="13" y2="16" stroke="var(--burgundy)" stroke-width="1.6"/><line x1="10" y1="13" x2="10" y2="16" stroke="var(--burgundy)" stroke-width="1.6"/><line x1="12" y1="10" x2="17" y2="1" stroke="var(--burgundy)" stroke-width="1.6"/></svg>
      </div>
      <div class="service-title">Web applications</div>
      <p class="service-text">Lorem Ipsum is simply dummy text of the printing and typesetting industry Lorem Ipsum</p>
    </div>
    <div class="service-divider" style="left:280px"></div>
    <div class="service" style="left:291px">
      <div class="service-icon">
        <svg width="18" height="18" viewBox="0 0 18 18" aria-hidden="true"><rect x="2" y="2" width="8" height="13" fill="none" stroke="var(--burgundy)" stroke-width="1.6"/><rect x="10" y="5" width="6" height="10" fill="none" stroke="var(--burgundy)" stroke-width="1.6"/><line x1="4" y1="6" x2="8" y2="6" stroke="var(--burgundy)" stroke-width="1.4"/><line x1="4" y1="9" x2="8" y2="9" stroke="var(--burgundy)" stroke-width="1.4"/></svg>
      </div>
      <div class="service-title">Enterprise content<br>management</div>
      <p class="service-text">Lorem Ipsum is simply dummy text of the printing and typesetting industry Lorem Ipsum</p>
    </div>
    <div class="service-divider" style="left:503px"></div>
    <div class="service" style="left:512px">
      <div class="service-icon">
        <svg width="18" height="18" viewBox="0 0 18 18" aria-hidden="true"><rect x="2" y="2" width="14" height="14" rx="2" fill="var(--burgundy)"/><rect x="8" y="5" width="2" height="8" fill="#fff"/><rect x="5" y="8" width="8" height="2" fill="#fff"/></svg>
      </div>
      <div class="service-title">Health<br>information technology</div>
      <p class="service-text">Lorem Ipsum is simply dummy text of the printing and typesetting industry Lorem Ipsum</p>
    </div>
    <div class="service-divider" style="left:722px"></div>
    <div class="service" style="left:733px">
      <div class="service-icon">
        <svg width="20" height="18" viewBox="0 0 20 18" aria-hidden="true"><rect x="2" y="3" width="16" height="11" fill="none" stroke="var(--burgundy)" stroke-width="1.6"/><rect x="5" y="6" width="3" height="5" fill="var(--burgundy)"/><rect x="9" y="8" width="3" height="3" fill="var(--burgundy)"/><rect x="13" y="5" width="3" height="6" fill="var(--burgundy)"/><line x1="7" y1="16" x2="13" y2="16" stroke="var(--burgundy)" stroke-width="1.6"/></svg>
      </div>
      <div class="service-title">Strategic IT solutions</div>
      <p class="service-text">Lorem Ipsum is simply dummy text of the printing and typesetting industry Lorem Ipsum</p>
    </div>
  </section>

  <svg class="hero-notch" width="20" height="10" viewBox="0 0 20 10" aria-hidden="true"><polygon points="0,10 10,0 20,10" fill="var(--panel)"/></svg>

  <section class="cta-band">
    <div class="cta-text"><span class="cta-lead">CLICK HERE</span> FOR VIEW MORE SERVICES</div>
    <svg class="cta-arrow" width="46" height="26" viewBox="0 0 46 26" aria-hidden="true">
      <path d="M4 24 C8 12 20 7 34 8" fill="none" stroke="rgba(255,255,255,0.45)" stroke-width="2"/>
      <polyline points="28,2 36,8 29,14" fill="none" stroke="rgba(255,255,255,0.45)" stroke-width="2"/>
    </svg>
    <div class="cta-button">VIEW MORE</div>
  </section>

  <section class="info">
    <h3 class="info-heading" style="left:84px; top:787px">Call us toll free:</h3>
    <div class="phone">1 555 010 2040</div>
    <p class="call-note">Lorem Ipsum<br>Simply dummy text<br>printing and typesetting<br>industry</p>
    <div class="call-link">Contact@KELTO</div>
    <div class="column-shadow"></div>

    <h3 class="info-heading" style="left:263px; top:787px">Need IT solutions?</h3>
    <p class="need-lead">Simply dummy text of the printing&nbsp; typesetting</p>
    <p class="need-copy">Lorem Ipsum is simply dummy text of the printing and typesetting industry Lorem Ipsum has been the industry's standard dummy text ever</p>
    <div class="team-photo" role="img" aria-label="Businessman in shirt and tie holding a laptop"></div>

    <svg class="quote-mark" width="22" height="18" viewBox="0 0 22 18" aria-hidden="true">
      <polygon points="4,0 10,0 6,18 0,18" fill="var(--burgundy)"/>
      <polygon points="15,0 21,0 17,18 11,18" fill="var(--burgundy)"/>
    </svg>
    <p class="quote-text">Lorem Ipsum is simply dummy text the printing and typesetting istry Lorem Ipsum has been the inustry's sta....</p>
    <p class="quote-author"><strong>Mark Dalton</strong>(simply dummy)</p>

    <h3 class="info-heading" style="left:664px; top:787px">Featured:</h3>
    <ul class="link-list" style="left:664px; top:819px">
      <li>Managed Services</li>
      <li>Virtual Office</li>
      <li>Starting Planning</li>
      <li>Mobile IT</li>
      <li>Network Security</li>
      <li>web applications</li>
    </ul>

    <h3 class="info-heading" style="left:806px; top:787px">Popular:</h3>
    <ul class="link-list" style="left:806px; top:819px">
      <li>Lorem Ipsum is simply</li>
      <li>Dummy text of the</li>
      <li>Typesetting</li>
      <li>Industry. Lorem</li>
      <li>Ipsum has been</li>
      <li>Industry's standard</li>
    </ul>
  </section>

  <footer class="site-footer">
    <div class="footer-rule"></div>
    <div class="footer-brand">
      <span class="footer-brand-square"></span>
      <span class="footer-brand-name">KELTO</span>
    </div>
    <span class="social-dot" style="left:83px"></span>
    <span class="social-dot" style="left:99px"></span>
    <div class="copyright">© Copyright 2014 - KELTO. All rights reserved.</div>

    <ul class="link-list footer-links" style="left:310px; top:1076px">
      <li>Home</li>
      <li>About Us</li>
      <li>Services</li>
      <li>Work</li>
      <li>Blog</li>
    </ul>
    <ul class="link-list footer-links" style="left:422px; top:1076px">
      <li>IT solutions</li>
      <li>enterprise content management</li>
      <li>health information technology</li>
      <li>web applications</li>
      <li>strategic IT solutions &amp; solutions architect</li>
    </ul>

    <div class="partner" style="left:688px; top:1084px; width:46px; height:22px"></div>
    <div class="partner" style="left:760px; top:1084px; width:72px; height:22px"></div>
    <div class="partner" style="left:856px; top:1084px; width:66px; height:22px"></div>
    <div class="partner" style="left:688px; top:1124px; width:88px; height:22px"></div>
    <div class="partner" style="left:800px; top:1124px; width:102px; height:22px"></div>
  </footer>

</div>
</body>
</html>
```